Postcard flyer for body postive dance classes

We need an eye catching double sided A6 postcard for body positive dance classes. The business name is stepbloomjoy and already have a rough logo and some text that needs tidying up and putting together. The design needs to be simple and elegant. We are appealing to a diverse range of adult women with or without dance experience to join us in a safe, supportive and creative environment. We would like the design to use black, white and a soft green. The final design should communicate movement, contentment and wholeness. File with information attached.

Target Market(s)

Diverse range of adult women

Industry/Entity Type

Health And Wellness

Font styles to use
Other font styles liked:
• Candara or similar but open to suggestions

Colors
abd036
cadf82
eaf2ce
fffefb
fef9ed
fff3d1
ffffff

Requirements
Must have
• Logo and text provided.
Nice to have
• Sense of movement. Match to website colours and style.
Should not have
• Intimidating perfect body images

```html
<!DOCTYPE html>
<html lang="en">
<head>
<meta charset="utf-8">
<title>stepbloomjoy postcard</title>
<link href="https://fonts.googleapis.com/css2?family=Lobster&family=Mulish:ital,wght@0,400;0,700;0,800;1,400&display=swap" rel="stylesheet">
<style>
  :root {
    --green: #abd036;
    --green-soft: #cadf82;
    --green-pale: #eaf2ce;
    --ink: #222222;
    --paper: #ffffff;
    --mist: #e6e6e6;
    --stage: #d6d6d6;
  }
  html, body {
    margin: 0;
    width: 1200px;
    height: 1200px;
    overflow: hidden;
    background: var(--stage);
    font-family: "Mulish", "Candara", sans-serif;
  }
  .postcard {
    position: absolute;
    left: 237px;
    width: 846px;
    height: 602px;
    transform: scale(0.858);
    transform-origin: 0 0;
    overflow: hidden;
    background: var(--paper);
  }
  .postcard--front { top: 62px; }
  .postcard--back { top: 620px; }
  .postcard__art { position: absolute; inset: 0; }
  .txt { position: absolute; margin: 0; line-height: 1; white-space: nowrap; color: var(--ink); }

  /* front */
  .brand { left: 300px; top: 98px; display: flex; align-items: center; gap: 18px; }
  .brand__dot { width: 46px; height: 46px; border: 3px solid var(--ink); border-radius: 50%; box-sizing: border-box; }
  .brand__name { font-size: 44px; font-weight: 400; color: var(--ink); line-height: 1; }
  .brand__tagline { left: 334px; top: 150px; font-size: 15px; }
  .headline { font-family: "Lobster", cursive; }
  .headline--joy { left: 118px; top: 184px; font-size: 68px; color: #2e2e2e; -webkit-text-stroke: 1.5px var(--green); text-shadow: 2px 3px 3px rgba(0,0,0,0.25); }
  .headline--love { left: 292px; top: 262px; font-size: 72px; color: var(--green); -webkit-text-stroke: 1.5px var(--ink); text-shadow: 2px 3px 3px rgba(0,0,0,0.25); }
  .front-core { left: 0; width: 846px; text-align: center; top: 376px; font-size: 22px; font-style: italic; }
  .front-celebration { left: 0; width: 846px; text-align: center; top: 489px; font-size: 22px; font-style: italic; }
  .front-web { left: 0; width: 846px; text-align: center; top: 569px; font-size: 14px; letter-spacing: 5px; color: var(--paper); }

  /* back */
  .intro { left: 56px; top: 57px; font-size: 20px; line-height: 24px; letter-spacing: 0.5px; }
  .reignite { left: 56px; top: 133px; font-size: 29px; font-weight: 800; color: var(--green); }
  .journey { left: 56px; top: 189px; font-size: 20px; line-height: 24px; letter-spacing: 0.5px; }
  .contact {
    position: absolute; left: 60px; top: 296px; width: 358px; height: 183px;
    box-sizing: border-box; border: 4px solid var(--ink); border-radius: 42px;
    background: linear-gradient(180deg, var(--green-soft) 0%, var(--green) 70%, #98bd26 100%);
    box-shadow: 0 6px 10px rgba(0,0,0,0.2);
  }
  .contact__title { position: absolute; left: 36px; top: 18px; margin: 0; font-size: 31px; font-weight: 800; text-decoration: underline; text-decoration-thickness: 2px; text-underline-offset: 4px; color: var(--ink); line-height: 1; }
  .contact__list { position: absolute; left: 36px; top: 64px; margin: 0; padding: 0; list-style: none; font-size: 18px; font-weight: 800; line-height: 23px; color: var(--ink); }
  .back-web { left: 64px; top: 568px; font-size: 15px; letter-spacing: 2px; }
</style>
</head>
<body>

<section class="postcard postcard--front" aria-label="Postcard front">
  <svg class="postcard__art" viewBox="0 0 846 602" width="846" height="602" role="img" aria-label="Light grey damask pattern panel framed by green and black curves">
    <defs>
      <linearGradient id="front-bg" x1="0" y1="0" x2="0" y2="1">
        <stop offset="0" stop-color="#f4f4f4"/>
        <stop offset="0.6" stop-color="#ffffff"/>
        <stop offset="1" stop-color="#e4e4e4"/>
      </linearGradient>
      <linearGradient id="medallion" x1="0" y1="0" x2="0" y2="1">
        <stop offset="0" stop-color="#e9e9e9"/>
        <stop offset="0.7" stop-color="#f3f3f3"/>
        <stop offset="1" stop-color="#ffffff"/>
      </linearGradient>
    </defs>
    <rect width="846" height="602" fill="url(#front-bg)"/>
    <rect width="846" height="200" fill="var(--green)"/>
    <path d="M0,178 C60,90 180,62 330,56 Q400,52 428,28 Q456,52 526,56 C676,62 790,90 846,170 V330 C790,402 680,422 530,427 Q460,432 428,466 Q396,432 326,427 C176,422 60,402 0,320 Z" fill="var(--green)" stroke="var(--ink)" stroke-width="24"/>
    <path d="M0,178 C60,90 180,62 330,56 Q400,52 428,28 Q456,52 526,56 C676,62 790,90 846,170 V330 C790,402 680,422 530,427 Q460,432 428,466 Q396,432 326,427 C176,422 60,402 0,320 Z" fill="none" stroke="var(--paper)" stroke-width="10"/>
    <path d="M0,182 C60,96 180,70 330,64 Q400,60 428,38 Q456,60 526,64 C676,70 790,96 846,176 V318 C790,388 680,408 530,413 Q460,418 428,450 Q396,418 326,413 C176,408 60,388 0,308 Z" fill="url(#medallion)"/>
    <ellipse cx="423" cy="352" rx="150" ry="4" fill="rgba(0,0,0,0.12)"/>
    <rect x="70" y="470" width="54" height="54" rx="10" fill="#cfcfcf" role="img" aria-label="Small floral flourish ornament"/>
    <rect x="726" y="470" width="54" height="54" rx="10" fill="#cfcfcf" role="img" aria-label="Small floral flourish ornament"/>
    <rect y="545" width="846" height="6" fill="var(--green)"/>
    <rect y="551" width="846" height="51" fill="var(--ink)"/>
  </svg>

  <div class="txt brand">
    <span class="brand__dot"></span>
    <span class="brand__name">stepbloomjoy</span>
  </div>
  <p class="txt brand__tagline">Movement, contentment, wholeness</p>
  <p class="txt headline headline--joy">Dance is joy</p>
  <p class="txt headline headline--love">Dance is love</p>
  <p class="txt front-core">Dance is at the core of our being</p>
  <p class="txt front-celebration">A celebration of movement, vitality and wholeness</p>
  <p class="txt front-web">www.stepbloomjoy.com.au</p>
</section>

<section class="postcard postcard--back" aria-label="Postcard back">
  <svg class="postcard__art" viewBox="0 0 846 602" width="846" height="602" role="img" aria-label="Light grey damask pattern panel beside a white address area with a wavy divider">
    <defs>
      <linearGradient id="back-bg" x1="0" y1="0" x2="0" y2="1">
        <stop offset="0" stop-color="#e6e6e6"/>
        <stop offset="0.5" stop-color="#f8f8f8"/>
        <stop offset="1" stop-color="#e2e2e2"/>
      </linearGradient>
    </defs>
    <rect width="846" height="602" fill="url(#back-bg)"/>
    <rect y="125" width="470" height="47" fill="var(--ink)"/>
    <ellipse cx="240" cy="282" rx="140" ry="4" fill="rgba(0,0,0,0.12)"/>
    <rect y="543" width="846" height="6" fill="var(--ink)"/>
    <rect y="549" width="846" height="53" fill="var(--green)"/>
    <path d="M503,0 C458,40 433,100 438,160 C443,230 513,260 518,330 C523,400 458,440 463,470 C468,520 508,570 533,602" fill="none" stroke="var(--green)" stroke-width="10"/>
    <path d="M515,0 C470,40 445,100 450,160 C455,230 525,260 530,330 C535,400 470,440 475,470 C480,520 520,570 545,602" fill="none" stroke="var(--ink)" stroke-width="22"/>
    <path d="M528,0 C483,40 458,100 463,160 C468,230 538,260 543,330 C548,400 483,440 488,470 C493,520 533,570 558,602 L846,602 L846,0 Z" fill="var(--paper)" stroke="var(--paper)" stroke-width="4"/>
    <rect x="707" y="44" width="99" height="99" fill="#c8c8c8" stroke="#333333" stroke-width="2"/>
  </svg>

  <p class="txt intro">If you’ve never danced before<br>and always wanted to</p>
  <p class="txt reignite">or you want to reignite</p>
  <p class="txt journey">your past love of dance,<br>join us at stepbloomjoy to start<br>your journey.</p>
  <div class="contact">
    <p class="contact__title">Contact us now!</p>
    <ul class="contact__list">
      <li>E: hello@stepbloomjoy.com.au</li>
      <li>P:0400518274</li>
      <li>www.stepbloomjoy.com.au</li>
      <li>Elmvale/Brookfield</li>
    </ul>
  </div>
  <p class="txt back-web">Please visit us at:www.stepbloomjoy.com.au</p>
</section>

</body>
</html>
```